Design a poster - 10 habits to follow for Natural Health

We need a poster to be made, containing the list of habits below along with the heading and other description. Please use good and free pics of green leafy vegetables from the net, attaching some related to every point.
Also need the Brightvale logo, website - www.brightvale-demo.com and the app download logos of playstore and app store. Attaching a sample poster with relevant files.
Please make it in a way that people share the poster with others on social media and put it as a checklist in their desks or kitchen. (to be able to read them everyday)

Poster text starts -

10 easy habits to start your Natural health journey
Small habits that you can start today to get in best state of your health. Try reading these once daily -
1. Reduce or Replace the Tea/Coffee/Milk intake – Start with replacing few intakes of tea/coffee with lemon, green or herbal tea. Check for herbal tea recipe on Brightvale.
2. Eat fruits as a service to your long terms health - Keep a large bowl of your favourites fruits in your living room for daily visibility and pick a fruit every time you feel like munching.
3. Reduce refined Sugar – Keep Jaggery handy in your kitchen or office cafe to replace white sugar.
4. Reduce table Salt – Keep rock salt handy in your kitchen to replace table salt.
5. Eat more Salads – Just keep adding number of salads you eat in a week. Even a regular peanut masala salad is good to start with. Reaching a state of only 2 cooked meals in a day is ideal.
6. Fasting sometimes – Start with 8pm to 8am fasting on some days, not that difficult to implement. This might do wonders to your health.
7. Eat more dry fruits and nuts (non-salted and fried) – Keep these handy in your kitchen & living room too.
8. Sun is the best doctor ever - Make it a point to soak some sunlight in morning or evening. Sun is the best doctor ever.
9. Sleep early – around 10pm. Lie down on your bed and start reading a book if you are not able to sleep. Keep the phone & other electronics away.
10. Reduce non-veg/animal food for some time - to notice the faster health improvement. Prefer eating veg whenever you can.
Pick one habit at a time, follow it for 10 days & then add the next. As you change your habits, your taste buds will change!! Which one you want to pick first, depends on you. Will say start with the easiest and then keep picking up more & more difficult ones.

- Poster text ends.

```html
<!DOCTYPE html>
<html lang="en">
<head>
<meta charset="utf-8">
<title>10 Easy Habits to Start Your Natural Health Journey</title>
<link rel="stylesheet" href="https://fonts.googleapis.com/css2?family=Kalam:wght@700&family=Arimo:wght@400;700&display=swap">
<style>
  :root {
    --ink: #1a1a1a;
    --paper: #ffffff;
    --orange: #e07b1a;
    --purple: #7a1f8a;
    --green: #2e9a3a;
    --blue: #1f6fb8;
    --gold: #b8860b;
    --red: #d8261c;
    --web: #f0d64a;
    --badge: #0d0d0d;
    --wood-dark: #3c2a1c;
    --wood-mid: #6b5038;
  }
  * { box-sizing: border-box; margin: 0; padding: 0; }
  html, body { width: 1200px; height: 716px; overflow: hidden; background: var(--paper); }
  body { font-family: "Arimo", Arial, sans-serif; color: var(--ink); }
  .poster { position: relative; width: 1200px; height: 716px; overflow: hidden; }

  .backdrop {
    position: absolute; inset: 0;
    background:
      radial-gradient(ellipse 420px 260px at 960px 250px, rgba(95,143,58,.85), transparent 70%),
      radial-gradient(ellipse 420px 220px at 600px 420px, rgba(150,112,70,.7), transparent 70%),
      linear-gradient(180deg, #8a7a66 0%, var(--wood-mid) 45%, var(--wood-dark) 100%);
  }

  .header {
    position: absolute; left: 19px; top: 24px; width: 944px; height: 116px;
    background: var(--paper); padding: 8px 10px;
  }
  .title {
    font-family: "Kalam", cursive; font-weight: 700; font-size: 31px;
    text-transform: uppercase; letter-spacing: .6px; line-height: 1.15; white-space: nowrap;
  }
  .subtitle { color: var(--orange); font-size: 19px; margin-top: 6px; }
  .instruction { color: var(--purple); font-size: 17px; margin-top: 5px; }

  .brand {
    position: absolute; left: 1063px; top: 0; width: 106px; height: 104px;
    background: var(--paper); display: flex; align-items: center; justify-content: center;
  }
  .brand-name { font-size: 15px; font-weight: 700; color: var(--ink); }

  .habit {
    position: absolute; width: 180px; height: 180px; border-radius: 50%; background: var(--paper);
    display: flex; flex-direction: column; align-items: center; justify-content: center;
    text-align: center; padding: 0 17px; font-size: 11px; line-height: 1.22;
    transform: translate(-50%, -50%);
  }
  .habit.wide { width: 195px; height: 195px; }
  .habit-num { font-family: "Kalam", cursive; font-size: 36px; line-height: .9; }
  .habit-name { font-size: 11px; margin: 2px 0 3px; }
  .c-green { color: var(--green); }
  .c-blue { color: var(--blue); }
  .c-purple { color: var(--purple); }
  .c-red { color: var(--red); }
  .c-gold { color: var(--gold); }

  .advice {
    position: absolute; left: 26px; top: 606px; width: 560px;
    color: var(--red); font-size: 11.5px; font-style: italic; line-height: 1.3;
  }
  .website { position: absolute; left: 28px; top: 686px; color: var(--web); font-size: 18px; }

  .store-badge {
    position: absolute; top: 644px; height: 63px;
    background: var(--badge); border: 2px solid #bfbfbf; border-radius: 9px;
  }
</style>
</head>
<body>
<main class="poster">
  <div class="backdrop" role="img" aria-label="Photo of a wicker basket of fresh vegetables, lettuce, beetroot and tomatoes on a wooden table"></div>

  <header class="header">
    <h1 class="title">10 Easy Habits to Start Your Natural Health Journey</h1>
    <p class="subtitle">Small habits that you can start today to get in best state of your health.</p>
    <p class="instruction">Try reading these once daily.</p>
  </header>

  <div class="brand"><span class="brand-name">Brightvale</span></div>

  <section class="habit" style="left:100px;top:262px">
    <span class="habit-num">1</span>
    <span class="habit-name c-green">Reduce or Replace the Tea/Coffee/Milk intake.</span>
    Start with replacing few intakes of tea/coffee with lemon, green or herbal tea. Check for herbal tea recipe on Brightvale.
  </section>

  <section class="habit" style="left:304px;top:262px">
    <span class="habit-num">2</span>
    <span class="habit-name c-blue">Eat fruits as a service to your long terms health.</span>
    Keep a large bowl of your favourites fruits in your living room for daily visibility and pick a fruit every time you feel like munching.
  </section>

  <section class="habit" style="left:503px;top:267px">
    <span class="habit-num">3</span>
    <span class="habit-name c-purple">Reduce refined Sugar.</span>
    Keep Jaggery handy in your kitchen or office cafe to replace white sugar.
  </section>

  <section class="habit" style="left:696px;top:262px">
    <span class="habit-num">4</span>
    <span class="habit-name c-purple">Reduce table Salt.</span>
    Keep rock salt handy in your kitchen to replace table salt.
  </section>

  <section class="habit wide" style="left:893px;top:280px">
    <span class="habit-num">5</span>
    <span class="habit-name c-green">Eat more Salads.</span>
    Just keep adding number of salads you eat in a week. Even a regular peanut masala salad is good to start with. Reaching a state of only 2 cooked meals in a day is ideal.
  </section>

  <section class="habit" style="left:184px;top:453px">
    <span class="habit-num">6</span>
    <span class="habit-name c-red">Fasting sometimes.</span>
    Start with 8pm to 8am fasting on some days, not that difficult to implement. This might do wonders to your health.
  </section>

  <section class="habit" style="left:395px;top:460px">
    <span class="habit-num">7</span>
    <span class="habit-name c-gold">Eat more dry fruits and nuts</span>
    (non-salted and fried). Keep these handy in your kitchen &amp; living room too.
  </section>

  <section class="habit" style="left:600px;top:473px">
    <span class="habit-num">8</span>
    <span class="habit-name c-blue">Sun is the best doctor ever.</span>
    Make it a point to soak some sunlight in morning or evening. Sun is the best doctor ever.
  </section>

  <section class="habit" style="left:807px;top:473px">
    <span class="habit-num">9</span>
    <span class="habit-name c-red">Sleep early</span>
    - around 10pm. Lie down on your bed and start reading a book if you are not able to sleep. Keep the phone &amp; other electronics away.
  </section>

  <section class="habit" style="left:1011px;top:460px">
    <span class="habit-num">10</span>
    <span class="habit-name c-purple">Reduce non-veg /animal food</span>
    for some time - to notice the faster health improvement. Prefer eating veg whenever you can.
  </section>

  <p class="advice">
    Pick one habit at a time, follow it for 10 days &amp; then add the next.<br>
    As you change your habits, your taste buds will change!!<br>
    Which one you want to pick first, depends on you.<br>
    Will say start with the easiest and then keep picking up more &amp; more difficult ones.
  </p>

  <p class="website">www.brightvale-demo.com</p>

  <div class="store-badge" style="left:728px;width:205px" aria-hidden="true"></div>
  <div class="store-badge" style="left:953px;width:214px" aria-hidden="true"></div>
</main>
</body>
</html>
```